Torvenu Business Card Design Project

We need a business card design for torvenu.com a company based in Berlin, Germany.

?Torvenu is marketplace that enables people all over the world to monetize and exchange their individual knowledge and language skills through interactive video sessions. User are matched by their interests.

On Torvenu everybody can be student or teacher (seller or buyer).

We would love to see designs that use or main color blue and green. The design should communicate what Torvenu enables - see my notice above.

Looking so forward to your designs
Cheers from Berlin,
Konrad

Target Market(s)

globally

Industry/Entity Type

Teacher

Requirements
Must have
• Konrad Wielert
CEO
Torvenu.com

Torvenu e-Services GmbH
Lindgrubweg 27
10117 Berlin

Fon: +49 30 481 906 27 14
Mobile: 49 171 57 04 91 3
E-Mail: k.wielert@torvenu.com
Web: www.torvenu.com

```html
<!DOCTYPE html>
<html lang="en">
<head>
<meta charset="utf-8">
<title>Torvenu Business Card</title>
<link rel="stylesheet" href="https://fonts.googleapis.com/css2?family=Jura:wght@400;500;600&display=swap">
<style>
  :root {
    --backdrop: #643200;
    --brand-blue: #02a3e0;
    --brand-green: #8dc63f;
    --paper: #ffffff;
    --ink-grey: #6a6a6a;
  }
  * { margin: 0; padding: 0; box-sizing: border-box; }
  html, body {
    width: 1200px;
    height: 402px;
    overflow: hidden;
    background: var(--backdrop);
    font-family: "Jura", "Segoe UI", sans-serif;
  }
  .canvas {
    position: relative;
    width: 1200px;
    height: 402px;
  }
  .card {
    position: absolute;
    top: 61px;
    width: 494px;
    height: 282px;
    border-radius: 26px;
    overflow: hidden;
  }
  /* Front */
  .card-front {
    left: 52px;
    background: var(--paper);
  }
  .front-stripe {
    position: absolute;
    left: 269px;
    top: 0;
    width: 4px;
    height: 100%;
    background: var(--brand-green);
  }
  .front-panel {
    position: absolute;
    left: 276px;
    top: 0;
    right: 0;
    height: 100%;
    background: var(--brand-blue);
    color: var(--paper);
  }
  .brand-lockup {
    position: absolute;
    left: 22px;
    top: 118px;
    display: flex;
    align-items: center;
    gap: 10px;
  }
  .brand-square {
    width: 30px;
    height: 30px;
    background: var(--brand-blue);
  }
  .brand-name {
    font-size: 40px;
    font-weight: 500;
    color: var(--ink-grey);
    line-height: 1;
  }
  .person-name {
    position: absolute;
    left: 30px;
    top: 43px;
    font-size: 17px;
    font-weight: 500;
    letter-spacing: 0.3px;
  }
  .person-role {
    position: absolute;
    left: 30px;
    top: 62px;
    font-size: 11px;
    font-style: italic;
  }
  .contact-list {
    position: absolute;
    left: 28px;
    top: 112px;
    list-style: none;
    font-size: 12.5px;
    line-height: 18.3px;
  }
  .company-address {
    position: absolute;
    left: 28px;
    top: 213px;
    font-size: 12.5px;
    line-height: 16.5px;
    font-style: normal;
  }
  /* Back */
  .card-back {
    left: 650px;
    background: var(--brand-blue);
    color: var(--paper);
  }
  .back-brand {
    position: absolute;
    left: 0;
    right: 0;
    top: 88px;
    display: flex;
    justify-content: center;
    align-items: center;
    gap: 16px;
  }
  .back-circle {
    width: 56px;
    height: 56px;
    border-radius: 50%;
    background: var(--paper);
  }
  .back-name {
    font-size: 64px;
    font-weight: 600;
    line-height: 1;
  }
  .back-web {
    position: absolute;
    left: 0;
    right: 0;
    top: 255px;
    text-align: center;
    font-size: 13.5px;
    letter-spacing: 0.3px;
  }
</style>
</head>
<body>
<main class="canvas">
  <section class="card card-front" aria-label="Business card front">
    <div class="brand-lockup">
      <span class="brand-square" aria-hidden="true"></span>
      <span class="brand-name">Torvenu</span>
    </div>
    <div class="front-stripe"></div>
    <div class="front-panel">
      <h1 class="person-name">Konrad Wielert</h1>
      <p class="person-role">CEO</p>
      <ul class="contact-list">
        <li>P : +49 30 481 906 27 14</li>
        <li>C : 49 171 57 04 91 3</li>
        <li>E : k.wielert@torvenu.com</li>
        <li>W : www.torvenu.com</li>
      </ul>
      <address class="company-address">
        Torvenu e-Services GmbH,<br>
        Lindgrubweg 27 10117 Berlin
      </address>
    </div>
  </section>

  <section class="card card-back" aria-label="Business card back">
    <div class="back-brand">
      <span class="back-circle" aria-hidden="true"></span>
      <span class="back-name">Torvenu</span>
    </div>
    <p class="back-web">www.website.com</p>
  </section>
</main>
</body>
</html>
```